Office Building Banner

Need a 4x8 vinyl banner made for our office/storage headquarters. Our branded colors and logo can be taken from our website, www.brightcrestroofingtx.com. All other elements of our brand have not been decided on yet, so you have creative autonomy there. Our location faces a busy highway in Seguin, Texas, so the banner needs to have our contact information and full name clearly seen from a bit away's away, hope that makes sense. Our company wants to convey attributes of strength, loyalty, protection - basically emulating the qualities of a wolf and his pack. I have uploaded a few items we have been using to date, but as you can see, graphic design is not our forte.

```html
<!DOCTYPE html>
<html lang="en">
<head>
<meta charset="utf-8">
<title>Brightcrest Roofing &amp; Renovation – Office Banner</title>
<link rel="stylesheet" href="https://fonts.googleapis.com/css2?family=Poppins:wght@500;600;700;800&display=swap">
<style>
  :root {
    --brand-orange: #f4511e;
    --brand-black: #111111;
    --brand-gray: #5a5a5a;
    --paper: #ffffff;
    --paper-shade: #ededed;
    --page-bg: #ffffff;
    --sky: #c9d5df;
    --lawn: #5f9b35;
    --siding: #8a8478;
  }
  html, body {
    margin: 0;
    padding: 0;
    width: 1200px;
    height: 2698px;
    overflow: hidden;
    background: var(--page-bg);
  }
  .banner {
    position: absolute;
    left: 50px;
    top: 249px;
    width: 1100px;
    height: 2200px;
    box-shadow: 0 20px 50px rgba(0,0,0,0.28);
    font-family: "Poppins", sans-serif;
  }
  .banner svg { display: block; width: 100%; height: 100%; }
  .headline-name { fill: var(--brand-orange); font-weight: 800; }
  .headline-service { fill: var(--brand-gray); font-weight: 700; }
  .headline-amp { fill: var(--brand-gray); font-weight: 500; }
  .headline-box-text { fill: var(--brand-orange); font-weight: 700; }
  .tagline { fill: var(--brand-black); font-weight: 600; }
  .call-label { fill: var(--brand-orange); font-weight: 700; }
  .phone { fill: var(--brand-black); font-weight: 700; }
  .web { fill: var(--paper); font-weight: 500; letter-spacing: 2px; }
  .web-accent { fill: var(--brand-orange); font-weight: 700; }
  .badge-name { fill: var(--brand-black); font-weight: 700; }
</style>
</head>
<body>
  <div class="banner">
    <svg viewBox="0 0 688 1375" xmlns="http://www.w3.org/2000/svg">
      <defs>
        <linearGradient id="paperGradient" x1="0" y1="0" x2="0" y2="1">
          <stop offset="0" stop-color="#ffffff"/>
          <stop offset="0.7" stop-color="#f2f2f2"/>
          <stop offset="1" stop-color="#e6e6e6"/>
        </linearGradient>
        <linearGradient id="photoGradient" x1="0" y1="0" x2="0" y2="1">
          <stop offset="0" stop-color="#c9d5df"/>
          <stop offset="0.3" stop-color="#a89c8c"/>
          <stop offset="0.62" stop-color="#8a8478"/>
          <stop offset="0.75" stop-color="#5f9b35"/>
          <stop offset="1" stop-color="#4f8a2a"/>
        </linearGradient>
      </defs>

      <!-- backdrop -->
      <rect class="paper" width="688" height="1375" fill="url(#paperGradient)"/>

      <!-- hero photo area -->
      <g role="img" aria-label="Photo of a two-storey suburban house with a new shingle roof, green lawn and trees">
        <path d="M0 0 H688 V470 Q520 452 336 520 Q170 565 0 528 Z" fill="url(#photoGradient)"/>
      </g>

      <!-- hero swooshes -->
      <path class="swoosh-orange" d="M336 520 Q520 452 688 470 V506 Q520 482 336 545 Z" fill="var(--brand-orange)"/>
      <path class="swoosh-black" d="M0 528 Q170 565 336 520 L336 535 Q170 578 0 562 Z" fill="var(--brand-black)"/>

      <!-- name badge -->
      <circle class="badge" cx="336" cy="475" r="138" fill="var(--paper)" stroke="var(--brand-orange)" stroke-width="3"/>
      <text class="badge-name" x="336" y="487" text-anchor="middle" font-size="34">BRIGHTCREST</text>

      <!-- headline -->
      <text class="headline-name" x="344" y="735" text-anchor="middle" font-size="84">BRIGHTCREST</text>
      <text x="344" y="828" text-anchor="middle" font-size="96">
        <tspan class="headline-service">ROOFING </tspan><tspan class="headline-amp">&amp;</tspan>
      </text>
      <rect class="headline-box" x="69" y="842" width="550" height="73" fill="var(--brand-black)"/>
      <text class="headline-box-text" x="344" y="903" text-anchor="middle" font-size="68">RENOVATION</text>

      <!-- tagline -->
      <text class="tagline" x="344" y="962" text-anchor="middle" font-size="35">Local Roofing Company</text>
      <text class="tagline" x="344" y="999" text-anchor="middle" font-size="35">Serving Greater, TX</text>

      <!-- call to action -->
      <text class="call-label" x="344" y="1077" text-anchor="middle" font-size="54">CALL US TODAY</text>
      <text class="phone" x="344" y="1158" text-anchor="middle" font-size="76">512-555-0148</text>

      <!-- footer band -->
      <path class="footer-accent" d="M245 1212 Q470 1240 688 1200 V1250 Q470 1275 300 1222 Z" fill="var(--brand-orange)"/>
      <path class="footer-band" d="M0 1225 Q120 1182 260 1210 Q470 1255 688 1248 V1375 H0 Z" fill="var(--brand-black)"/>
      <text x="344" y="1316" text-anchor="middle" font-size="31">
        <tspan class="web">www.</tspan><tspan class="web web-accent">brightcrestroofingtx</tspan><tspan class="web">.com</tspan>
      </text>
    </svg>
  </div>
</body>
</html>
```